Business Cards for cafe providing speciality coffee and food

I need a business card design for my husband’s businesses. He has two cafes in Brisbane. The business name is Copperleaf Roasting House. They sell high end specialty coffee as well as breakfast and lunch. All the food is cooked fresh, in house and they have strict quality controls for their coffee. I would like the business card to feature the address for both cafes, my husband’s phone number and the business’s instagram. The address for the first is 61 Walden Crescent, Oakvale and the second is 23 Pellow Avenue, Brindlemoor. The Instagram handle is @copperleafroastinghouse and phone number is 0491362847. We already have a business logo that is attached.

Target Market(s)

All ages, higher disposable income and more likely to eat out regularly

Industry/Entity Type

Hospitality

Contact Information for Business Card

Must be suitable for both customers and suppliers

Font styles to use
Sans Serif

Colors

Designer to choose colors to be used in the design.

Requirements
Must have
• Owner’s name: Reid Castell
• Addresses of both cafes: 61 Walden Crescent, Oakvale and 23 Pellow Avenue, Brindlemoor
• Instagram handle: @copperleafroastinghouse
• Contact number: 0491362847
Nice to have
• Business logo

```html
<!DOCTYPE html>
<html lang="en">
<head>
<meta charset="utf-8">
<title>Copperleaf Roasting House – Business Cards</title>
<link href="https://fonts.googleapis.com/css2?family=Montserrat:wght@400;500&family=Poiret+One&display=swap" rel="stylesheet">
<style>
  :root {
    --page: #d9d9d9;
    --ink: #1e1f1f;
    --paper: #fbfbfa;
    --light: #f4f4f2;
  }
  * { margin: 0; padding: 0; box-sizing: border-box; }
  html, body { width: 1200px; height: 900px; overflow: hidden; }
  body {
    position: relative;
    background: var(--page);
    font-family: "Montserrat", sans-serif;
  }
  .card {
    position: absolute;
    width: 630px;
    height: 360px;
    border-radius: 4px;
    box-shadow: 0 10px 30px rgba(0,0,0,0.25);
    overflow: hidden;
  }
  .card-front { left: 110px; top: 60px; background: var(--ink); }
  .card-back  { left: 460px; top: 480px; background: var(--paper); }

  .brand-mark {
    position: absolute;
    left: 50%; top: 50%;
    transform: translate(-50%, -50%);
    display: flex; flex-direction: column; align-items: center; gap: 14px;
    color: var(--light);
  }
  .brand-ring {
    width: 120px; height: 120px; border-radius: 50%;
    border: 3px solid var(--light);
  }
  .brand-name {
    font-weight: 500; font-size: 17px; letter-spacing: 3px;
    text-transform: uppercase; text-align: center;
  }

  .name-tab {
    position: absolute;
    left: 60px; top: 0;
    width: 190px; height: 270px;
    background: var(--ink);
    border-radius: 0 0 95px 95px;
    display: flex; flex-direction: column; align-items: center;
    color: var(--light);
  }
  .owner-name {
    margin-top: 40px;
    font-family: "Poiret One", sans-serif;
    font-size: 26px; letter-spacing: 1.5px;
    text-transform: uppercase;
  }
  .tab-brand {
    margin-top: 26px;
    display: flex; flex-direction: column; align-items: center; gap: 8px;
  }
  .tab-ring { width: 70px; height: 70px; border-radius: 50%; border: 2px solid var(--light); }
  .tab-brand-name {
    font-size: 10px; font-weight: 500; letter-spacing: 1.5px;
    text-transform: uppercase; text-align: center; line-height: 1.4;
  }

  .contact-list {
    position: absolute;
    right: 28px; top: 120px;
    list-style: none;
    color: var(--ink);
    font-size: 15px;
    text-align: right;
  }
  .contact-item { display: flex; align-items: center; justify-content: flex-end; gap: 10px; margin-bottom: 12px; }
  .contact-icon {
    width: 20px; height: 20px; border-radius: 50%;
    background: var(--ink);
    display: flex; align-items: center; justify-content: center;
  }
  .addresses {
    position: absolute;
    right: 28px; bottom: 42px;
    font-size: 14px; color: var(--ink);
    letter-spacing: 0.2px;
  }
  .addresses .divider { margin: 0 8px; }
</style>
</head>
<body>

<section class="card card-front" aria-label="Card front">
  <div class="brand-mark">
    <div class="brand-ring"></div>
    <div class="brand-name">Copperleaf Roasting House</div>
  </div>
</section>

<section class="card card-back" aria-label="Card back">
  <div class="name-tab">
    <h1 class="owner-name">Reid Castell</h1>
    <div class="tab-brand">
      <div class="tab-ring"></div>
      <div class="tab-brand-name">Copperleaf<br>Roasting House</div>
    </div>
  </div>

  <ul class="contact-list">
    <li class="contact-item">
      <span>0491362847</span>
      <span class="contact-icon">
        <svg width="12" height="12" viewBox="0 0 24 24" aria-hidden="true">
          <path fill="#f4f4f2" d="M6.6 10.8a15.1 15.1 0 0 0 6.6 6.6l2.2-2.2a1 1 0 0 1 1-.25 11.4 11.4 0 0 0 3.6.57 1 1 0 0 1 1 1V20a1 1 0 0 1-1 1A17 17 0 0 1 3 4a1 1 0 0 1 1-1h3.5a1 1 0 0 1 1 1c0 1.25.2 2.45.57 3.57a1 1 0 0 1-.25 1z"/>
        </svg>
      </span>
    </li>
    <li class="contact-item">
      <span>@copperleafroastinghouse</span>
      <span class="contact-icon"></span>
    </li>
  </ul>

  <p class="addresses">
    61 Walden Crescent, Oakvale<span class="divider">/</span>23 Pellow Avenue, Brindlemoor
  </p>
</section>

</body>
</html>
```